Pet removal of legal foothold or snare traps trifold

A trifold that plainly describes how to remove your pet from a foot hold trap, Cable restraint or snare. Integrated with the Keystone Fieldcraft Guild logo,website and basic information about trapping.

Target Market(s)

Pet Owners ,General public ,outdoor enthusiasts ,hikers ,campers etc.

Industry/Entity Type

Legal

Requirements
Must have
• Keystone Fieldcraft Guild logo and website www.fieldcraftguild-example.org
• Pictures showing how to open a snare or cable restraint
• Pictures showing how to open a coil spring or long spring foothold trap
Nice to have
• I have some designs but I can't get them to download here I can email them to you
Should not have
• Anything that could be construed as anti-trapping

```html
<!DOCTYPE html>
<html lang="en">
<head>
<meta charset="utf-8">
<title>Releasing Pets From Traps – Trifold</title>
<link href="https://fonts.googleapis.com/css2?family=Oswald:wght@500;600&family=Open+Sans:ital,wght@0,400;0,600;1,400&display=swap" rel="stylesheet">
<style>
:root{
  --green:#2f9a12;
  --green-bright:#3cb516;
  --dark:#1f1f1f;
  --dark-2:#2b2b2b;
  --paper:#ffffff;
  --paper-grey:#ededed;
  --ink:#222;
  --canvas:#e2e2e2;
  --blue:#3a9fd8;
}
*{box-sizing:border-box;margin:0;padding:0}
html,body{width:1200px;height:1200px;overflow:hidden}
body{background:var(--canvas);font-family:"Open Sans",Arial,sans-serif;color:var(--ink);position:relative}
.sheet{position:absolute;left:200px;width:800px;height:571px;background:var(--paper);overflow:hidden}
.sheet--outside{top:17px}
.sheet--inside{top:612px}
.sheet-bg{position:absolute;inset:0}
.abs{position:absolute}
.photo{position:absolute}
.framed{border:4px solid var(--green)}
.headline{font-family:"Oswald",Impact,sans-serif;font-weight:600;text-transform:uppercase;line-height:1;letter-spacing:-0.5px}
.green{color:var(--green)}
.bar-url{position:absolute;top:536px;height:22px;width:264px;line-height:22px;text-align:center;color:#fff;font-size:9px;font-weight:600;letter-spacing:2.4px}
.body-copy{font-size:9.3px;line-height:12.2px;text-align:justify}
.steps p{margin-bottom:9px}
.steps b{color:var(--green);font-weight:600}
.intro{color:#fff;font-style:italic;font-size:8.7px;line-height:12px;text-align:justify}
.intro p{margin-bottom:8px}
.badge{position:absolute;border-radius:50%;display:flex;align-items:center;justify-content:center;text-align:center;font-family:"Oswald",Impact,sans-serif;font-weight:600;text-transform:uppercase;line-height:1.1}
.badge--light{background:#fff;border:4px solid var(--green);color:var(--green);font-size:15px}
.badge--blue{background:var(--blue);border:6px solid #fff;color:#fff;font-size:16px}
.contact-tab{position:absolute;background:#fff;border-radius:6px;box-shadow:0 2px 6px rgba(0,0,0,.35);text-align:center;padding-top:6px}
.contact-tab .headline{font-size:28px}
.org{font-size:13px;color:var(--green);text-align:center;text-transform:uppercase;line-height:16px}
.url{font-size:13.5px;color:#fff;text-align:center;font-weight:600}
</style>
</head>
<body>

<!-- Outside of the trifold -->
<section class="sheet sheet--outside">
  <svg class="sheet-bg" width="800" height="571" viewBox="0 0 800 571">
    <defs>
      <linearGradient id="greyPanel" x1="0" y1="0" x2="0" y2="1">
        <stop offset="0" stop-color="#e6e6e6"/><stop offset="1" stop-color="#fafafa"/>
      </linearGradient>
    </defs>
    <rect x="0" y="0" width="272" height="571" fill="#fff"/>
    <path d="M0,250 C90,226 190,212 272,222 V248 C190,240 90,250 0,275 Z" fill="#e9e9e9"/>
    <path d="M0,262 C90,236 190,224 272,232" stroke="var(--green)" stroke-width="7" fill="none"/>
    <rect x="272" y="0" width="264" height="571" fill="var(--dark)"/>
    <path d="M272,0 H536 V300 C500,270 440,250 380,242 C330,236 300,236 272,238 Z" fill="var(--green)"/>
    <rect x="536" y="0" width="264" height="571" fill="url(#greyPanel)"/>
    <circle cx="660" cy="272" r="130" fill="var(--green)"/>
    <circle cx="674" cy="266" r="124" fill="var(--dark-2)"/>
    <circle cx="670" cy="270" r="118" fill="#fff"/>
    <rect x="0" y="536" width="272" height="22" fill="var(--green)"/>
    <rect x="536" y="536" width="264" height="22" fill="var(--green)"/>
  </svg>

  <div class="photo" style="left:34px;top:16px;width:201px;height:166px;background:linear-gradient(#fff,#f0f0f0);border:1px dashed #bbb" role="img" aria-label="Line drawing of a coil spring foothold trap with arrows: 1. depress levers, 2. open jaws, 3. pull free"></div>
  <div class="badge badge--light" style="left:69px;top:198px;width:124px;height:124px">Keystone<br>Fieldcraft<br>Guild</div>

  <div class="abs body-copy steps" style="left:27px;top:330px;width:219px">
    <p><b>1.</b> Apply downward pressure to each of the trap levers. If you have sufficient hand strength, hold the trap with both hands using the heels of the palms to support each corner of the base and depress the levers simultaneously by squeezing with your fingers. Another method is to position the trap firmly on the ground and use your feet to simultaneously depress the levers.</p>
    <p><b>2.</b> When the levers are fully (or even partially) depressed, the trap jaws will open easily.</p>
    <p><b>3.</b> While depressing the levers, simply pull the trap free of the paw.</p>
  </div>
  <div class="bar-url" style="left:0;width:272px">www.fieldcraftguild-example.org</div>

  <div class="abs intro" style="left:290px;top:25px;width:226px">
    <p>Foothold traps are designed to capture furbearers securely by the paw and hold them alive and unharmed until the trapper arrives. Because of this, there is minimal risk of injury to your pet and the situation should prove to be nothing more than a minor inconvenience.</p>
    <p>Some dogs may unexpectedly bite when their paw or the trap is manipulated. If you are unsure how the dog will react when you try to open the trap, it is best to find another person to help. It will not pose any danger to your dog to be in a foothold trap for a short period of time while you locate help. Remember, your dog is going to be fine so it is important to remain calm. Do not make a hasty decision which might result in you or someone else getting severely injured from a dog bite.</p>
  </div>
  <div class="contact-tab" style="left:344px;top:265px;width:120px;height:80px">
    <div class="headline green">Contact</div>
    <div class="headline" style="color:var(--dark)">Us Now!</div>
  </div>
  <div class="abs org" style="left:272px;top:361px;width:264px">Keystone Fieldcraft<br>Guild</div>
  <div class="abs url" style="left:272px;top:399px;width:264px;font-size:11.5px">www.fieldcraftguild-example.org</div>
  <div class="photo framed" style="left:304px;top:425px;width:201px;height:118px;background:linear-gradient(#9a7a5a,#c9b9a2 60%,#7f8a60)" role="img" aria-label="Photo of a trapper standing beside rows of hanging furs outside a barn"></div>

  <div class="abs headline" style="left:536px;top:50px;width:264px;text-align:center;font-size:27px;line-height:30px">
    <span class="green">Releasing pets from</span><br><span style="color:var(--dark)">traps in Pennsylvania</span>
  </div>
  <div class="photo" style="left:557px;top:157px;width:226px;height:226px;border-radius:50%;background:radial-gradient(circle at 45% 40%,#e8d6c8,#9b7760 55%,#4a3328)" role="img" aria-label="Photo of a smiling woman hugging a brown puppy"></div>
  <div class="badge badge--light" style="left:606px;top:348px;width:122px;height:122px">Keystone<br>Fieldcraft<br>Guild</div>
  <div class="abs headline" style="left:536px;top:488px;width:264px;text-align:center;font-size:32px;color:var(--dark)">Foothold Traps</div>
  <div class="bar-url" style="left:536px">www.fieldcraftguild-example.org</div>
</section>

<!-- Inside of the trifold -->
<section class="sheet sheet--inside">
  <svg class="sheet-bg" width="800" height="571" viewBox="0 0 800 571">
    <defs>
      <linearGradient id="lynx" x1="0" y1="0" x2="0" y2="1">
        <stop offset="0" stop-color="#8c7a66"/><stop offset="1" stop-color="#c8b9a6"/>
      </linearGradient>
      <linearGradient id="coyote" x1="0" y1="0" x2="0" y2="1">
        <stop offset="0" stop-color="#a69a8a"/><stop offset="1" stop-color="#e6e6ea"/>
      </linearGradient>
      <linearGradient id="midPanel" x1="0" y1="0" x2="1" y2="0">
        <stop offset="0" stop-color="#e9e9e9"/><stop offset=".3" stop-color="#fff"/>
      </linearGradient>
    </defs>
    <rect x="0" y="0" width="272" height="571" fill="#fff"/>
    <rect x="272" y="0" width="264" height="571" fill="url(#midPanel)"/>
    <path d="M0,378 C100,402 200,378 272,340 V571 H0 Z" fill="var(--dark)"/>
    <path d="M0,372 C100,396 200,372 272,334" stroke="var(--green)" stroke-width="6" fill="none"/>
    <path role="img" aria-label="Close-up photo of a bobcat face" d="M272,340 C370,300 450,292 536,288 V571 H272 Z" fill="url(#lynx)"/>
    <path d="M272,336 C370,296 450,288 536,284" stroke="var(--green)" stroke-width="6" fill="none"/>
    <rect role="img" aria-label="Photo of a coyote lying in snow" x="536" y="0" width="264" height="310" fill="url(#coyote)"/>
    <path d="M536,318 C620,306 720,296 800,272 V571 H536 Z" fill="var(--dark)"/>
    <path d="M536,314 C620,302 720,292 800,268" stroke="var(--green)" stroke-width="6" fill="none"/>
    <rect x="0" y="536" width="272" height="22" fill="var(--green)"/>
    <rect x="536" y="536" width="264" height="22" fill="var(--green)"/>
  </svg>

  <div class="abs headline green" style="left:30px;top:28px;font-size:22px">Cable Restraints</div>
  <div class="photo" style="left:39px;top:58px;width:165px;height:98px;background:linear-gradient(#fff,#f0f0f0);border:1px dashed #bbb" role="img" aria-label="Line drawing showing how to locate the lock and feed the cable back through it"></div>
  <div class="abs body-copy" style="left:30px;top:169px;width:210px">Similarly to foothold traps, cable restraints are designed to capture furbearers alive and unharmed. The difference lies in what part of the animal is secured. A foothold trap holds an animal by the paw, whereas a cable restraint secures it around the neck. A fox or coyote caught in a cable restraint is restrained in a very similar manner as a dog is held on a leash or tether.</div>
  <div class="photo framed" style="left:31px;top:282px;width:198px;height:93px;background:linear-gradient(#7f8a5c,#a89478 60%,#6f7a4c)" role="img" aria-label="Photo of a coyote held by a cable restraint"></div>
  <div class="abs headline" style="left:0;top:440px;width:272px;text-align:center;font-size:36px;line-height:39px">
    <span style="color:#fff">Our image is</span><br><span class="green" style="color:var(--green-bright)">our future</span>
  </div>
  <div class="bar-url" style="left:0;width:272px">www.fieldcraftguild-example.org</div>

  <div class="abs body-copy" style="left:295px;top:30px;width:214px">These Guild training programs also stress ethics and responsibility, and cover every aspect of trapping from proper trap adjustment to proper fur handling. These programs assure future and novice trappers understand proper use of trapping devices as well as their responsibility as Guild trappers. In addition, trapping equipment may also be used for wildlife research or the control of wildlife and human conflicts.</div>
  <div class="photo framed" style="left:299px;top:169px;width:199px;height:86px;background:linear-gradient(#ffffff,#dcdcdc)" role="img" aria-label="Photo of two foothold traps with chains"></div>

  <div class="badge badge--blue" style="left:681px;top:183px;width:166px;height:166px;margin-left:-136px">Keystone<br>Fieldcraft<br>Guild</div>
  <div class="abs headline" style="left:536px;top:362px;width:264px;text-align:center;font-size:36px;line-height:38px">
    <span class="green" style="color:var(--green-bright)">Contact</span><br><span style="color:#fff">Us Now!</span>
  </div>
  <div class="abs org" style="left:536px;top:451px;width:264px">Keystone Fieldcraft<br>Guild</div>
  <div class="abs url" style="left:536px;top:490px;width:264px;font-size:11.5px">www.fieldcraftguild-example.org</div>
  <div class="bar-url" style="left:536px">www.fieldcraftguild-example.org</div>
</section>

</body>
</html>
```